Stationary KV Relay
business card, letterhead, envelopes, email signature,memo pad and invoice/quotes
Project: Stationary KV Relay
Stationary KV Relay   - Telecommunications
Creative Brief
Use same font as used in my logo
or any
Bright & Fun-filled
Tom Variscoff
CEO
3F B28 GALERI NUSAPARK JAKARTA PUSAT 14071
tom@kvrelay.com
www.kvrelay.com
Feel free to utilize different styles but try to stick to the company logo colors as best as possible.
Require: Business card, Stationary, Envelopes, Invoice, E-mail signature & Notepad
pwarnet pwarnet
EPS format upload already
brightoak brightoak
definitely!! but there is lots of designs please rate my design so i will easy to make the stationary of your like designs thanks :)
Business card, Stationary, Envelopes, Invoice, E-mail signature & Notepad
Check your private massage! thanks!
nice for this time

```html
<!DOCTYPE html>
<html lang="en">
<head>
<meta charset="utf-8">
<title>KV Relay – Business Card</title>
<link rel="stylesheet" href="https://fonts.googleapis.com/css2?family=Exo+2:wght@400;600;800&display=swap">
<style>
  :root {
    --bg: #d9dadc;
    --card: #ffffff;
    --blue: #1d4fa8;
    --blue-deep: #0f3680;
    --blue-light: #3f7fd6;
    --orange: #f5a81c;
    --orange-deep: #e8850f;
    --ink: #3b4656;
    --muted: #6d7684;
  }
  * { box-sizing: border-box; margin: 0; padding: 0; }
  html, body { width: 1200px; height: 984px; overflow: hidden; }
  body {
    background: var(--bg);
    font-family: "Exo 2", sans-serif;
    color: var(--ink);
    position: relative;
  }
  .card {
    position: absolute;
    width: 760px;
    height: 420px;
    background: var(--card);
    border-radius: 30px;
    box-shadow: 0 14px 30px rgba(0,0,0,.18);
    overflow: hidden;
  }
  .card-back { left: 330px; top: 50px; }
  .card-front { left: 110px; top: 514px; }

  /* back */
  .back-brand {
    position: absolute; left: 0; right: 0; top: 140px;
    display: flex; justify-content: center; align-items: center; gap: 16px;
  }
  .brand-dot {
    width: 54px; height: 54px; border-radius: 50%;
    background: var(--blue);
  }
  .brand-name {
    font-weight: 800; font-size: 46px; color: var(--blue);
    letter-spacing: 1px;
  }
  .back-web {
    position: absolute; left: 0; right: 0; top: 270px;
    text-align: center; font-size: 15px; letter-spacing: 9px;
    color: var(--muted);
  }

  /* front */
  .front-brand {
    position: absolute; left: 56px; top: 46px;
    display: flex; align-items: center; gap: 14px;
  }
  .front-brand .brand-dot { width: 48px; height: 48px; }
  .front-brand .brand-name { font-size: 40px; }
  .holder {
    position: absolute; left: 78px; top: 132px;
  }
  .holder-name { font-size: 17px; font-weight: 600; letter-spacing: 2px; color: var(--blue); }
  .holder-role { font-size: 13px; letter-spacing: 2px; color: var(--muted); margin-top: 3px; }
  .address {
    position: absolute; left: 78px; top: 196px;
    font-size: 13px; letter-spacing: 2px; line-height: 1.7; color: var(--ink);
  }
  .contacts {
    position: absolute; left: 392px; top: 136px;
    list-style: none; font-size: 14px; letter-spacing: 1.5px; color: var(--ink);
  }
  .contacts li { display: flex; align-items: center; gap: 10px; height: 24px; }
  .contacts svg { width: 16px; height: 16px; flex: none; }
  .wave { position: absolute; left: 0; bottom: 0; width: 760px; height: 170px; }
</style>
</head>
<body>

<section class="card card-back" aria-label="Business card back">
  <div class="back-brand">
    <span class="brand-dot"></span>
    <span class="brand-name">KV Relay</span>
  </div>
  <p class="back-web">www.kvrelay.com</p>
</section>

<section class="card card-front" aria-label="Business card front">
  <div class="front-brand">
    <span class="brand-dot"></span>
    <span class="brand-name">KV Relay</span>
  </div>

  <div class="holder">
    <p class="holder-name">Tom Variscoff</p>
    <p class="holder-role">CEO</p>
  </div>

  <p class="address">3F B28 GALERI NUSAPARK<br>JAKARTA PUSAT 14071</p>

  <ul class="contacts">
    <li>
      <svg viewBox="0 0 16 16"><circle cx="8" cy="8" r="8" fill="var(--blue)"/><path d="M5.2 4.2l1.6 0 .6 2-1 .8a6 6 0 0 0 2.6 2.6l.8-1 2 .6v1.6c-3.6.6-7.2-3-6.6-6.6z" fill="#fff"/></svg>
      +621-480-555-210
    </li>
    <li>
      <svg viewBox="0 0 16 16"><circle cx="8" cy="8" r="8" fill="var(--blue)"/><path d="M5.2 4.2l1.6 0 .6 2-1 .8a6 6 0 0 0 2.6 2.6l.8-1 2 .6v1.6c-3.6.6-7.2-3-6.6-6.6z" fill="#fff"/></svg>
      +628-517-300-114
    </li>
    <li>
      <svg viewBox="0 0 16 16"><circle cx="8" cy="8" r="8" fill="var(--blue)"/><rect x="4" y="5" width="8" height="6" rx="1" fill="#fff"/><path d="M4.3 5.4L8 8.3l3.7-2.9" stroke="var(--blue)" stroke-width="1" fill="none"/></svg>
      tom@kvrelay.com
    </li>
    <li>
      <svg viewBox="0 0 16 16"><circle cx="8" cy="8" r="8" fill="var(--blue)"/><circle cx="8" cy="8" r="4" stroke="#fff" stroke-width="1.2" fill="none"/><path d="M4 8h8M8 4c-2 2.4-2 5.6 0 8M8 4c2 2.4 2 5.6 0 8" stroke="#fff" stroke-width="1" fill="none"/></svg>
      www.kvrelay.com
    </li>
  </ul>

  <svg class="wave" viewBox="0 0 760 170" preserveAspectRatio="none" aria-hidden="true">
    <defs>
      <linearGradient id="blueFill" x1="0" y1="0" x2="1" y2="1">
        <stop offset="0" stop-color="var(--blue-light)"/>
        <stop offset="0.6" stop-color="var(--blue)"/>
        <stop offset="1" stop-color="var(--blue-deep)"/>
      </linearGradient>
      <linearGradient id="orangeLine" x1="0" y1="0" x2="1" y2="0">
        <stop offset="0" stop-color="var(--orange-deep)"/>
        <stop offset="1" stop-color="var(--orange)"/>
      </linearGradient>
    </defs>
    <path d="M0 60 C 200 150, 480 150, 760 20 L 760 170 L 0 170 Z" fill="url(#blueFill)"/>
    <path d="M0 46 C 210 140, 480 138, 760 6" stroke="url(#orangeLine)" stroke-width="7" fill="none"/>
  </svg>
</section>

</body>
</html>
```